High Tech Software Startup needs Letterhead Design

We need a letterhead for a startup company base in Brazil. The letterhead should combine with our logo attached here.
We are a team of professionals in Java for web and mobile with iOS and android development.
We are looking for a modern and futuristc design.

Target Market(s)

CIO, IT managers of mid to big size companies

Industry/Entity Type

It Company

```html
<!DOCTYPE html>
<html lang="pt-BR">
<head>
<meta charset="utf-8">
<title>Veltra – Papel Timbrado</title>
<link rel="stylesheet" href="https://fonts.googleapis.com/css2?family=Ubuntu:wght@400;500;700&display=swap">
<style>
  :root {
    --backdrop: #e9e9ea;
    --paper: #ffffff;
    --navy: #0c3a5c;
    --ink: #1d2b45;
    --brand-blue: #1f74ad;
    --band-light: #c3d6e6;
    --band-lilac: #d5d6e8;
    --stripe: #c4c5dc;
  }
  * { box-sizing: border-box; margin: 0; padding: 0; }
  html, body {
    width: 1039px; height: 1200px; overflow: hidden;
    background: var(--backdrop);
    font-family: "Ubuntu", sans-serif;
  }
  .letterhead {
    position: absolute; left: 143px; top: 64px;
    width: 752px; height: 1072px;
    background: var(--paper);
    box-shadow: 0 2px 10px rgba(0,0,0,.12);
    overflow: hidden;
  }
  .brand {
    position: absolute; left: 28px; top: 34px;
    display: flex; align-items: center; gap: 16px;
  }
  .brand-square {
    width: 72px; height: 72px; border-radius: 6px;
    background: var(--brand-blue);
  }
  .brand-name {
    font-weight: 700; font-size: 66px; line-height: 1;
    color: var(--navy); letter-spacing: 1px;
  }
  .contact-divider {
    position: absolute; left: 469px; top: 42px;
    width: 1.5px; height: 50px; background: var(--navy);
  }
  .contact-list {
    position: absolute; left: 488px; top: 44px;
    list-style: none; font-size: 14px; color: var(--ink);
  }
  .contact-list li {
    display: flex; align-items: center; gap: 11px; height: 16.5px;
  }
  .contact-list svg { width: 13px; height: 13px; fill: var(--ink); flex: none; }
  .footer-shapes { position: absolute; left: 0; bottom: 0; width: 752px; height: 86px; }
  .address {
    position: absolute; left: 0; width: 752px; top: 1011px;
    text-align: center; font-size: 14px; font-weight: 500;
    line-height: 17px; color: var(--ink); padding-left: 60px;
  }
  .address span { margin-left: 10px; }
</style>
</head>
<body>
  <main class="letterhead">
    <header>
      <div class="brand">
        <div class="brand-square"></div>
        <div class="brand-name">VELTRA</div>
      </div>
      <div class="contact-divider"></div>
      <ul class="contact-list">
        <li>
          <svg viewBox="0 0 24 24"><path d="M6.6 10.8a15.1 15.1 0 0 0 6.6 6.6l2.2-2.2a1 1 0 0 1 1-.25 11.4 11.4 0 0 0 3.6.57 1 1 0 0 1 1 1V20a1 1 0 0 1-1 1A17 17 0 0 1 3 4a1 1 0 0 1 1-1h3.5a1 1 0 0 1 1 1c0 1.25.2 2.45.57 3.57a1 1 0 0 1-.25 1z"/></svg>
          (11) 5555-0142
        </li>
        <li>
          <svg viewBox="0 0 24 24"><path d="M12 2a10 10 0 1 0 0 20 10 10 0 0 0 0-20zm6.9 6h-2.9a15.6 15.6 0 0 0-1.4-3.6A8 8 0 0 1 18.9 8zM12 4c.8 1.2 1.5 2.5 1.9 4h-3.8c.4-1.5 1.1-2.8 1.9-4zM4.3 14a8 8 0 0 1 0-4h3.4a16 16 0 0 0 0 4zm.8 2h2.9c.3 1.3.8 2.5 1.4 3.6A8 8 0 0 1 5.1 16zM8 8H5.1a8 8 0 0 1 4.3-3.6C8.8 5.5 8.3 6.7 8 8zm4 12c-.8-1.2-1.5-2.5-1.9-4h3.8c-.4 1.5-1.1 2.8-1.9 4zm2.3-6H9.7a14.7 14.7 0 0 1 0-4h4.6a14.7 14.7 0 0 1 0 4zm.3 5.6c.6-1.1 1.1-2.3 1.4-3.6h2.9a8 8 0 0 1-4.3 3.6zm1.7-5.6a16 16 0 0 0 0-4h3.4a8 8 0 0 1 0 4z"/></svg>
          www.veltra.com.br
        </li>
        <li>
          <svg viewBox="0 0 24 24"><path d="M2 9l10-7 10 7v12H2zm2 2.2V19h16v-7.8l-8 5.3z"/></svg>
          contato@veltra.com.br
        </li>
      </ul>
    </header>

    <svg class="footer-shapes" viewBox="0 0 752 86" aria-hidden="true">
      <defs>
        <linearGradient id="band-fill" x1="0" y1="0" x2="1" y2="0">
          <stop offset="0" stop-color="var(--band-light)"/>
          <stop offset="1" stop-color="var(--band-lilac)"/>
        </linearGradient>
      </defs>
      <path d="M0 86 C10 40 60 2 130 2 L574 2 L252 86 Z" fill="url(#band-fill)"/>
      <path d="M702 2 L752 2 L752 16 L622 86 L572 86 Z" fill="var(--stripe)"/>
    </svg>

    <address class="address" style="font-style:normal">
      <div>Rua das Acácias, 318 &nbsp;9º. Andar &nbsp;Conj. 904 <span>Caixa Postal &nbsp;221</span></div>
      <div>Jardim Aurora &nbsp;&nbsp;CEP &nbsp;04.512-300</div>
      <div>São Paulo - SP - Brasil</div>
    </address>
  </main>
</body>
</html>
```